Criação de Papelaria Profissional para Construção & Engenharia
" Fabricamos estruturas metálicas para Armazéns Graneleiros, Unidades de Beneficiamento de Sementes, Garagem para máquinas agrícolas, Classificação, etc "

```html
<!DOCTYPE html>
<html lang="pt-BR">
<head>
<meta charset="utf-8">
<title>Martelli Metalurgia e Engenharia — Cartão</title>
<link rel="stylesheet" href="https://fonts.googleapis.com/css2?family=Roboto+Condensed:wght@700&display=swap">
<style>
  :root {
    --page-bg: #ece9e4;
    --card-black: #121212;
    --brand-red: #e0232a;
    --white: #ffffff;
    --spark-light: #f6a53a;
    --spark-mid: #b45a1c;
    --spark-dark: #2a1a12;
  }
  html, body {
    margin: 0;
    padding: 0;
    width: 1200px;
    height: 1200px;
    overflow: hidden;
    background: var(--page-bg);
  }
  .canvas {
    position: relative;
    width: 1200px;
    height: 1200px;
  }
  .card {
    position: absolute;
    left: 50px;
    top: 391px;
    width: 1100px;
    height: 418px;
    box-shadow: 0 10px 30px rgba(0,0,0,0.25);
  }
  .card svg { display: block; }
  .brand-name {
    font-family: "Roboto Condensed", "Arial Narrow", sans-serif;
    font-weight: 700;
    font-size: 54px;
    fill: var(--white);
    letter-spacing: 2px;
  }
  .brand-tagline {
    font-family: "Roboto Condensed", "Arial Narrow", sans-serif;
    font-weight: 700;
    font-size: 18px;
    fill: var(--white);
    letter-spacing: 1.5px;
  }
</style>
</head>
<body>
<main class="canvas">
  <section class="card">
    <svg width="1100" height="418" viewBox="0 0 1100 418" xmlns="http://www.w3.org/2000/svg">
      <defs>
        <linearGradient id="sparkTones" x1="0" y1="0" x2="1" y2="0.6">
          <stop offset="0" stop-color="var(--spark-dark)"/>
          <stop offset="0.35" stop-color="var(--spark-mid)"/>
          <stop offset="0.7" stop-color="var(--spark-light)"/>
          <stop offset="1" stop-color="var(--spark-mid)"/>
        </linearGradient>
      </defs>
      <rect class="card-bg" x="0" y="0" width="1100" height="418" fill="var(--card-black)"/>
      <polygon class="card-photo" points="0,0 532,0 398,418 0,418" fill="url(#sparkTones)"
               role="img" aria-label="Fotografia de serralheiro cortando metal com esmerilhadeira, faíscas laranja"/>
      <g class="brand-lockup">
        <text class="brand-name" x="810" y="224" text-anchor="middle">MARTELLI</text>
        <text class="brand-tagline" x="810" y="256" text-anchor="middle">METALURGIA E ENGENHARIA</text>
      </g>
      <path class="accent-bar" d="M624,418 L624,404 Q624,396 632,396 L1020,396 Q1028,396 1028,404 L1028,418 Z" fill="var(--brand-red)"/>
    </svg>
  </section>
</main>
</body>
</html>
```